Brookvale Holdings Ltd - Logo and Business Card

Create a logo and business card design for our new company.

Canadian private investment company with holdings in Saskatchewan Oil and real-estate.

Target Market(s)

Investors

Industry/Entity Type

Finance

Contact Information for Business Card

Name - Dominic Harlow
Position - President
Phone - 306.482.7159
Website - www.brookvaleholdings.ca

Logo Text

Today. Tomorrow. Together. (Tag Line)

Colors

Designer to choose colors to be used in the design.

Requirements
Must have
• Logo Must Have - Type Font only
• Must be modern, professional and stand out from the crowd.
Nice to have
• Don't have any, blank slate.

```html
<!DOCTYPE html>
<html lang="en">
<head>
<meta charset="utf-8">
<title>Brookvale Holdings Ltd – Business Card</title>
<link href="https://fonts.googleapis.com/css2?family=Cinzel:wght@400;600&family=Open+Sans:wght@400;600&display=swap" rel="stylesheet">
<style>
  :root {
    --backdrop: #222222;
    --card-light: #f2f2f2;
    --card-green: #58a60a;
    --brand-orange: #e0921a;
    --brand-green: #4f9a12;
    --ink: #2b2b2b;
    --white: #ffffff;
  }
  * { margin: 0; padding: 0; box-sizing: border-box; }
  html, body {
    width: 1200px; height: 900px; overflow: hidden;
    background: var(--backdrop);
  }
  .stage { position: relative; width: 1200px; height: 900px; }
  .card {
    position: absolute; top: 170px;
    width: 347px; height: 561px;
  }
  .card--front { left: 259px; background: var(--card-light); }
  .card--back { left: 631px; background: var(--card-green); }

  .brand {
    position: absolute; left: 0; right: 0;
    text-align: center;
    font-family: "Cinzel", serif;
    font-weight: 400;
  }
  .brand__mark {
    display: block; margin: 0 auto 18px;
    width: 70px; height: 70px; border-radius: 50%;
  }
  .brand__name { font-size: 38px; line-height: 1; letter-spacing: 0.5px; }
  .brand__suffix {
    font-size: 15px; letter-spacing: 6px; margin-top: 8px; padding-left: 6px;
  }
  .card--front .brand { top: 94px; color: var(--brand-orange); }
  .card--front .brand__mark { background: var(--brand-orange); }
  .card--back .brand { top: 200px; color: var(--white); }
  .card--back .brand__mark { background: var(--white); }

  .contact {
    position: absolute; left: 0; right: 0; top: 392px;
    text-align: center;
    font-family: "Open Sans", sans-serif;
  }
  .contact__name {
    font-family: "Cinzel", serif; font-weight: 600;
    font-size: 19px; letter-spacing: 0.3px;
  }
  .contact__first { color: var(--brand-orange); }
  .contact__last { color: var(--brand-green); }
  .contact__role { font-size: 14px; color: var(--ink); margin-top: 2px; }
  .contact__rule {
    width: 104px; height: 1px; margin: 22px auto 20px;
    background: var(--brand-orange); border: 0;
  }
  .contact__phone { font-size: 14px; color: var(--ink); }
  .contact__label { color: var(--brand-orange); font-weight: 600; }
  .contact__web { font-size: 14px; color: var(--brand-orange); margin-top: 2px; }
  .contact__web-domain { color: var(--brand-green); }
</style>
</head>
<body>
  <main class="stage">
    <section class="card card--front" aria-label="Business card front">
      <div class="brand">
        <span class="brand__mark"></span>
        <div class="brand__name">BROOKVALE</div>
        <div class="brand__suffix">HOLDINGS LTD</div>
      </div>
      <div class="contact">
        <div class="contact__name"><span class="contact__first">DOMINIC</span> <span class="contact__last">HARLOW</span></div>
        <div class="contact__role">President</div>
        <hr class="contact__rule">
        <div class="contact__phone"><span class="contact__label">P:</span> 306.482.7159</div>
        <div class="contact__web">www.<span class="contact__web-domain">brookvaleholdings</span>.ca</div>
      </div>
    </section>

    <section class="card card--back" aria-label="Business card back">
      <div class="brand">
        <span class="brand__mark"></span>
        <div class="brand__name">BROOKVALE</div>
        <div class="brand__suffix">HOLDINGS LTD</div>
      </div>
    </section>
  </main>
</body>
</html>
```